Business Card Design - Crisp & Clean

Looking for a new clean and crisp business card design. Design must incorporate our corporate colors (see attached style sheet). We're a pretty fun loving group who likes to keep it light while still portraying a professional image. Card should incorporate both our logo and our mascot (see attachment). Card should be double sided and should have room for our social media - Gleamrow, Brisk Hub and Zumbly on the back. Font selections do not have to match the style guide.

```html
<!DOCTYPE html>
<html lang="en">
<head>
<meta charset="utf-8">
<title>BrightCrew Business Card – Dana Holloway</title>
<link rel="stylesheet" href="https://fonts.googleapis.com/css2?family=Oswald:wght@400;500&family=Open+Sans:ital,wght@0,600;0,700;0,800;1,300;1,700&display=swap">
<style>
  :root {
    --card-white: #ffffff;
    --brand-yellow: #f7e600;
    --brand-blue: #5680c4;
    --swoosh-dark: #86878c;
    --swoosh-light: #f2f2f3;
    --ink: #111111;
    --accent-orange: #f0622a;
    --url-grey: #8e8e90;
    --mascot-shirt: #eeeeee;
    --mascot-skin: #e8c6a4;
  }
  html, body {
    margin: 0;
    padding: 0;
    width: 1200px;
    height: 686px;
    overflow: hidden;
    background: var(--card-white);
  }
  .card {
    position: relative;
    width: 1200px;
    height: 686px;
    background: var(--card-white);
    overflow: hidden;
    font-family: "Open Sans", Arial, sans-serif;
  }
  .card__swoosh {
    position: absolute;
    inset: 0;
  }
  .brand {
    position: absolute;
    left: 70px;
    top: 92px;
    display: flex;
    align-items: center;
    gap: 22px;
  }
  .brand__dot {
    width: 120px;
    height: 120px;
    border-radius: 50%;
    background: var(--brand-yellow);
  }
  .brand__name {
    margin: 0;
    font-weight: 800;
    font-size: 62px;
    line-height: 1;
    letter-spacing: -1px;
    color: var(--ink);
  }
  .brand__tagline {
    margin: 8px 0 0 4px;
    font-weight: 700;
    font-size: 17.5px;
    letter-spacing: 0.2px;
    color: var(--ink);
  }
  .mascot {
    position: absolute;
    left: 212px;
    top: 303px;
    width: 118px;
    height: 274px;
    border-radius: 50px 50px 18px 18px;
    background: linear-gradient(180deg, var(--mascot-shirt) 0%, var(--mascot-skin) 45%, var(--mascot-shirt) 60%, #3b2a22 100%);
  }
  .website {
    position: absolute;
    left: 94px;
    top: 580px;
    margin: 0;
    font-family: "Oswald", "Arial Narrow", sans-serif;
    font-weight: 400;
    font-size: 46px;
    line-height: 1;
    color: var(--url-grey);
  }
  .person {
    position: absolute;
    right: 57px;
    top: 214px;
    text-align: right;
  }
  .person__name {
    margin: 0;
    font-family: "Oswald", "Arial Narrow", sans-serif;
    font-weight: 500;
    font-size: 58px;
    line-height: 1.1;
    color: var(--brand-yellow);
  }
  .person__role {
    margin: 6px 0 0;
    font-style: italic;
    font-weight: 300;
    font-size: 40px;
    line-height: 1.1;
    color: var(--card-white);
  }
  .contact {
    position: absolute;
    right: 57px;
    top: 460px;
    text-align: right;
    font-weight: 600;
  }
  .contact__email {
    margin: 0;
    font-size: 40px;
    line-height: 1.2;
    color: var(--ink);
  }
  .contact__phone {
    margin: 12px 0 0;
    font-size: 40px;
    line-height: 1.2;
  }
  .contact__label {
    font-style: italic;
    font-weight: 700;
    font-size: 34px;
    color: var(--ink);
  }
  .contact__number {
    font-weight: 700;
    color: var(--accent-orange);
  }
</style>
</head>
<body>
<main class="card">
  <svg class="card__swoosh" width="1200" height="686" viewBox="0 0 1200 686" aria-hidden="true">
    <defs>
      <linearGradient id="swooshGrey" x1="0.3" y1="0.2" x2="1" y2="1">
        <stop offset="0" stop-color="var(--swoosh-dark)"/>
        <stop offset="0.45" stop-color="#a3a4a8"/>
        <stop offset="1" stop-color="var(--swoosh-light)"/>
      </linearGradient>
    </defs>
    <path d="M1145,20 C860,62 545,330 524,686 L546,686 C590,340 880,95 1200,34 L1200,24 Z" fill="var(--brand-blue)"/>
    <path d="M1200,42 C910,100 615,340 564,686 L1200,686 Z" fill="url(#swooshGrey)"/>
  </svg>

  <header class="brand">
    <div class="brand__dot"></div>
    <div class="brand__text">
      <p class="brand__name">BrightCrew</p>
      <p class="brand__tagline">HR PROCESS MANAGEMENT SOLUTIONS</p>
    </div>
  </header>

  <div class="mascot" role="img" aria-label="Company mascot illustration: cartoon professor in a white polo shirt and dark trousers"></div>

  <p class="website">www.brightcrew.com</p>

  <section class="person">
    <h1 class="person__name">Dana Holloway</h1>
    <p class="person__role">Marketing Wizard</p>
  </section>

  <section class="contact">
    <p class="contact__email">dana@brightcrew.com</p>
    <p class="contact__phone"><span class="contact__label">Mobile:</span> <span class="contact__number">555-214-7788</span></p>
  </section>
</main>
</body>
</html>
```